Flyer Design Project for our Parenting Psychologists at the Bright Harbour Wellbeing Clinic

At the Bright Harbour Wellbeing Clinic we have expert Parenting Psychologists.

Parenting Psychologists provide practical, step by step assistance to parents who are struggling with their children's behavioural and emotional problems.

We need a DL size brochure that will be appealing to parents. The brochure will be on show in schools, kindergartens and GP clinics.

In terms of style it will be in line with our website and stationery that I will attach.

www.brightharbourwellbeing.com.au
Updates

Hi Everyone,
Thanks for putting forward your proposals, there are a couple there that I am very interested in. I am looking to see if there is a way that I can change my brief to guaranteed as I am definitely going to be using one of the designs for sure.
I have emailed ArtFolkly and as soon as I get an answer I will change it if I can.
If anyone out there already knows the answer please let me know :-)
Thanks,
Marnie.

Hi Again,

I worked it out myself!!

I have now changed this to a committed project.

Kind regards,
Marnie.

Reason: I have 46 designs now and need more time to work out which is best!

Target Market(s)

The target will be educated professional parents motivated to get professional help. And doctors and teachers who will pass on the brochures 2 parents

Industry/Entity Type

Health

Requirements
Must have
• I want one DL size brochure. Back and front.

We need text (below) and our contact details. Our logo.

9362 4158
Suite 4, 2071 Pellbrook Rd, Ferndale Heights 3542

Text:
Parents want the best for their kids. They want kids that are happy, healthy and well behaved.

So why is it so hard? Parents of toddlers, primary schoolers and teenagers alike say that they are frustrated by constant nagging, bribing and yelling, they don't know what to try next. Some parents worry that their children are unhappy. Struggling at school, not making friends or coping with bigger problems.

The good news is that getting your children to behave more co-operatively doesn't need to be difficult or mysterious. We all know that kids don't come with manuals, but there are skills every parent can learn to make parenting easier. In a few sessions with a Parenting Psychologist, you will receive step by step guidance in how to talk to your children in a way that will be much more effective getting them to behave in a respectful and co-operative way around the home and in public. You will learn how to help your child cope with problems they are going through. They can help you reconnect with your kids so you can enjoy being a parent again.

Nice to have
• Themes consistent with our website
and letterhead, business cards. I will attach these.
Should not have
• I don't want it to look too cluttered so if the text I have provided up above looks too crowded then I will edit it.

```html
<!DOCTYPE html>
<html lang="en">
<head>
<meta charset="utf-8">
<title>Bright Harbour Wellbeing Clinic – Parenting Psychologist Flyer</title>
<link rel="stylesheet" href="https://fonts.googleapis.com/css2?family=Open+Sans:ital,wght@0,300;0,400;0,600;0,700;1,400&display=swap">
<style>
  :root {
    --green: #4f8a76;
    --teal-deep: #3c6568;
    --teal-light: #5fb6bf;
    --slate: #7d8a90;
    --olive: #8e9b82;
    --charcoal: #474c50;
    --ink: #555b5f;
    --paper: #ffffff;
    --mist: #eef0f0;
    --backdrop: #d9dcdd;
  }
  * { box-sizing: border-box; margin: 0; padding: 0; }
  html, body { width: 1148px; height: 1200px; overflow: hidden; }
  body {
    background: var(--backdrop);
    font-family: "Open Sans", Arial, sans-serif;
    color: var(--ink);
    position: relative;
  }
  .flyer {
    position: absolute;
    top: 50px;
    width: 520px;
    height: 1100px;
    background: var(--paper);
    overflow: hidden;
    box-shadow: 0 6px 20px rgba(0,0,0,.18);
  }
  .flyer--front { left: 36px; }
  .flyer--back { left: 592px; }

  .colour-strip { display: flex; height: 24px; }
  .colour-strip span { flex: 1; }
  .colour-strip span:nth-child(6n+1) { background: var(--teal-light); }
  .colour-strip span:nth-child(6n+2) { background: var(--slate); }
  .colour-strip span:nth-child(6n+3) { background: var(--green); }
  .colour-strip span:nth-child(6n+4) { background: var(--teal-deep); }
  .colour-strip span:nth-child(6n+5) { background: var(--charcoal); }
  .colour-strip span:nth-child(6n+6) { background: var(--olive); }

  /* Front */
  .front-photo {
    position: absolute; left: 0; top: 200px; width: 520px; height: 560px;
    background: radial-gradient(ellipse at 45% 40%, #f6dcc8 0%, #eac3a6 40%, #d9c08e 70%, #eeeeee 100%);
  }
  .front-head-bg { position: absolute; left: 0; top: 0; width: 520px; height: 200px; background: var(--paper); }
  .front-header {
    position: absolute; left: 0; top: 0; width: 520px; height: 176px;
    background: var(--paper);
    border-bottom-right-radius: 40px;
    border-left: 22px solid var(--green);
    padding: 20px 0 0 22px;
    z-index: 2;
  }
  .front-header h1 { font-weight: 300; font-size: 62px; line-height: 1; color: var(--ink); letter-spacing: -0.5px; }
  .front-header p { font-weight: 300; font-size: 40px; line-height: 1.3; color: var(--ink); }
  .front-strip { position: absolute; left: 0; top: 176px; width: 520px; z-index: 1; }
  .front-tagline {
    position: absolute; left: 0; top: 690px; width: 520px; height: 120px;
    background: var(--teal-deep);
    border-top-right-radius: 40px;
    color: var(--paper);
    padding: 24px 0 0 30px;
    z-index: 2;
  }
  .front-tagline strong { display: block; font-weight: 400; font-size: 36px; line-height: 1.1; }
  .front-tagline span { display: block; font-size: 24px; margin-top: 4px; }
  .front-brand {
    position: absolute; left: 0; top: 810px; width: 520px; height: 160px;
    background: linear-gradient(180deg, #f4f5f5 0%, #dcdfe0 100%);
    display: flex; align-items: center; padding-left: 60px; gap: 22px;
  }
  .brand-dot { width: 58px; height: 58px; border-radius: 50%; background: var(--teal-light); flex: none; }
  .brand-name { font-size: 26px; font-weight: 400; letter-spacing: 3px; line-height: 1.25; color: var(--charcoal); text-transform: uppercase; }
  .front-contact {
    position: absolute; left: 0; top: 970px; width: 520px; height: 130px;
    background: var(--green); color: var(--paper);
    padding: 22px 0 0 30px;
  }
  .front-contact .phone { font-size: 38px; font-weight: 700; }
  .front-contact .web { font-size: 21px; margin-top: 4px; }

  /* Back */
  .back-body { padding: 22px 28px 0 34px; }
  .back-body h2 { font-size: 40px; font-weight: 700; color: var(--green); margin-bottom: 12px; }
  .photo-round { border-radius: 50%; border: 8px solid var(--mist); }
  .photo-boy {
    float: right; width: 230px; height: 230px; margin: 40px -70px 10px 14px;
    shape-outside: circle(50%);
    background: radial-gradient(circle at 50% 40%, #d8b89a 0%, #9aa39a 55%, #f2f2f2 100%);
  }
  .photo-family {
    float: left; width: 240px; height: 240px; margin: 16px 14px 10px -70px;
    shape-outside: circle(50%);
    background: radial-gradient(circle at 45% 45%, #e8c9b0 0%, #8b7e6d 50%, #ecebe6 100%);
  }
  .intro { font-style: italic; font-size: 19px; line-height: 1.45; color: var(--ink); }
  .good-news { clear: right; margin-top: 26px; font-size: 19px; line-height: 1.5; text-align: right; color: var(--ink); }
  .good-news b { color: var(--green); font-weight: 700; }
  .back-footer {
    position: absolute; left: 0; top: 940px; width: 520px; height: 136px;
    border-top: 4px solid var(--mist);
    padding: 16px 28px 0 34px;
    background: var(--paper);
  }
  .footer-row { display: flex; justify-content: space-between; align-items: flex-start; }
  .footer-brand { display: flex; align-items: center; gap: 12px; }
  .footer-brand .brand-dot { width: 34px; height: 34px; }
  .footer-brand .brand-name { font-size: 14px; letter-spacing: 2px; }
  .footer-address { font-size: 13px; line-height: 1.4; text-align: right; color: var(--charcoal); }
  .footer-phone { font-size: 36px; font-weight: 700; color: var(--charcoal); margin-top: 8px; }
  .back-bottom-strip { position: absolute; left: 0; bottom: 0; width: 520px; }
</style>
</head>
<body>

<section class="flyer flyer--front">
  <div class="front-head-bg"></div>
  <div class="front-photo" role="img" aria-label="Photo of a smiling young girl with braided hair"></div>
  <header class="front-header">
    <h1>Parents want</h1>
    <p>the best for their kids.</p>
  </header>
  <div class="colour-strip front-strip"><span></span><span></span><span></span><span></span><span></span><span></span><span></span><span></span></div>
  <div class="front-tagline">
    <strong>They want kids that are</strong>
    <span>happy, healthy and well behaved.</span>
  </div>
  <div class="front-brand">
    <div class="brand-dot"></div>
    <div class="brand-name">Bright Harbour<br>Wellbeing Clinic</div>
  </div>
  <div class="front-contact">
    <div class="phone">Call on : (03) 9362 4158</div>
    <div class="web">www.brightharbourwellbeing.com.au</div>
  </div>
</section>

<section class="flyer flyer--back">
  <div class="colour-strip"><span></span><span></span><span></span><span></span><span></span><span></span><span></span><span></span></div>
  <div class="back-body">
    <h2>So why is it so hard?</h2>
    <div class="photo-round photo-boy" role="img" aria-label="Photo of a boy pouting while an adult points at him"></div>
    <p class="intro">Parents of toddlers, primary schoolers and teenagers alike say that they are frustrated by constant nagging, bribing and yelling, they don't know what to try next. Some parents worry that their children are unhappy. Struggling at school, not making friends or coping with bigger problems.</p>
    <div class="photo-round photo-family" role="img" aria-label="Photo of a mother helping her son with homework"></div>
    <p class="good-news"><b>The good news</b> is that getting your children to behave more co-operatively doesn't need to be difficult or mysterious. We all know that kids don't come with manuals, but there are skills every parent can learn to make parenting easier. In a few sessions with a Parenting Psychologist, you will receive step by step guidance in how to talk to your children in a way that will be much more effective getting them to behave in a respectful and co-operative way around the home and in public. You will learn how to help your child cope with problems they are going through. They can help you reconnect with your kids so you can enjoy being a parent again.</p>
  </div>
  <footer class="back-footer">
    <div class="footer-row">
      <div class="footer-brand">
        <div class="brand-dot"></div>
        <div class="brand-name">Bright Harbour<br>Wellbeing Clinic</div>
      </div>
      <div class="footer-address">Suite 4, 2071 Pellbrook Rd,<br>Ferndale Heights 3542<br>www.brightharbourwellbeing.com.au</div>
    </div>
    <div class="footer-phone">call on : (03) 9362 4158</div>
  </footer>
  <div class="colour-strip back-bottom-strip"><span></span><span></span><span></span><span></span><span></span><span></span><span></span><span></span></div>
</section>

</body>
</html>
```